Korbin Ventilation's. "We're Dalton beyond the pack"!

Good day< Does your company do face mask? that is question 1. and lets finish the stationary design and I will pay for that now? 2 If your company has BLACK HATS now I would want to do some of those? 3 I notice do you do BANNER'S and or something I can put on van's magnet type or on a building! )k that's enough but for now lets start with the stationary stuff? let me know you should have my information, and the design look's GREAT!!! Thank you..

```html
<!DOCTYPE html>
<html lang="en">
<head>
<meta charset="utf-8">
<title>Korbin Ventilation's – Letterhead</title>
<link rel="stylesheet" href="https://fonts.googleapis.com/css2?family=Lato:wght@300;400;700&family=Montserrat:wght@400;700&family=Pinyon+Script&display=swap">
<style>
  :root {
    --backdrop: #e3e3e3;
    --paper-top: #f6f6f6;
    --paper-bottom: #ececec;
    --brand-green: #9aab3f;
    --brand-black: #1c1c1c;
    --body-text: #3a3a3a;
    --heading-text: #111111;
  }
  * { margin: 0; padding: 0; box-sizing: border-box; }
  html, body {
    width: 1200px;
    height: 1200px;
    overflow: hidden;
    background: var(--backdrop);
  }
  .letterhead {
    position: absolute;
    left: 210px;
    top: 50px;
    width: 779px;
    height: 1100px;
    background: linear-gradient(180deg, var(--paper-top), var(--paper-bottom));
    box-shadow: 0 6px 18px rgba(0, 0, 0, 0.14);
    overflow: hidden;
    font-family: "Lato", sans-serif;
    color: var(--body-text);
  }
  .brand {
    position: absolute;
    left: 58px;
    top: 22px;
    width: 210px;
    text-align: center;
    font-family: "Montserrat", sans-serif;
    font-weight: 700;
    color: var(--brand-black);
  }
  .brand-dot {
    display: block;
    width: 60px;
    height: 60px;
    margin: 0 auto 10px;
    border-radius: 50%;
    background: var(--brand-black);
  }
  .brand-name {
    font-size: 22px;
    line-height: 1.05;
    letter-spacing: 0.5px;
    text-transform: uppercase;
  }
  .brand-tagline {
    margin-top: 6px;
    font-size: 12px;
  }
  .sender {
    position: absolute;
    left: 520px;
    top: 53px;
    font-family: "Montserrat", sans-serif;
    font-size: 12.5px;
    line-height: 15.5px;
    color: #444;
  }
  .sender-name {
    color: var(--brand-green);
    font-weight: 700;
  }
  .contact-list {
    list-style: none;
    margin-top: 12px;
  }
  .contact-list li {
    display: flex;
    align-items: center;
    gap: 7px;
    height: 16px;
  }
  .contact-icon {
    width: 11px;
    height: 11px;
    flex: none;
  }
  .accent-bar {
    position: absolute;
    right: 0;
    top: 51px;
    width: 12px;
    height: 111px;
    background: var(--brand-green);
  }
  .letter {
    position: absolute;
    left: 83px;
    top: 238px;
    width: 612px;
    font-size: 12.5px;
    font-weight: 300;
    line-height: 18.3px;
  }
  .date { margin-bottom: 18px; }
  .recipient { margin-bottom: 37px; }
  .recipient-name { font-weight: 700; color: var(--heading-text); }
  .salutation { margin-bottom: 18px; }
  .letter-body p {
    text-align: justify;
    margin-bottom: 18.3px;
  }
  .closing {
    margin-top: 46px;
  }
  .signature {
    font-family: "Pinyon Script", cursive;
    font-size: 25px;
    color: var(--heading-text);
    margin-top: 4px;
  }
  .footer-wedge {
    position: absolute;
    left: 0;
    bottom: 0;
    width: 779px;
    height: 122px;
  }
</style>
</head>
<body>
  <main class="letterhead">
    <header>
      <div class="brand">
        <span class="brand-dot" aria-hidden="true"></span>
        <div class="brand-name">Korbin<br>Ventilation's</div>
        <div class="brand-tagline">"We're Dalton beyond the pack"</div>
      </div>

      <address class="sender" style="font-style: normal;">
        <div class="sender-name">Korbin Ventilation GmbH &amp; Co</div>
        <div>City/State, Alder Road</div>
        <div>PO Box, Zip 4000, Australia</div>
        <ul class="contact-list">
          <li>
            <svg class="contact-icon" viewBox="0 0 24 24" aria-hidden="true"><path fill="#9aab3f" d="M6.6 10.8a15.1 15.1 0 0 0 6.6 6.6l2.2-2.2a1 1 0 0 1 1-.25 11.4 11.4 0 0 0 3.6.57 1 1 0 0 1 1 1V20a1 1 0 0 1-1 1A17 17 0 0 1 3 4a1 1 0 0 1 1-1h3.5a1 1 0 0 1 1 1c0 1.25.2 2.45.57 3.57a1 1 0 0 1-.25 1z"/></svg>
            <span>555.010.4200</span>
          </li>
          <li>
            <svg class="contact-icon" viewBox="0 0 24 24" aria-hidden="true"><path fill="#9aab3f" d="M2 5h20v14H2z"/><path fill="none" stroke="#f2f2f2" stroke-width="2" d="M2 5l10 8 10-8"/></svg>
            <span>info@korbinventilation.com</span>
          </li>
          <li>
            <svg class="contact-icon" viewBox="0 0 24 24" aria-hidden="true"><circle cx="12" cy="12" r="10" fill="none" stroke="#9aab3f" stroke-width="2"/><path fill="none" stroke="#9aab3f" stroke-width="1.6" d="M2 12h20M12 2c3 3 3 17 0 20M12 2c-3 3-3 17 0 20"/></svg>
            <span>www.korbinventilation.com</span>
          </li>
        </ul>
      </address>
      <div class="accent-bar" aria-hidden="true"></div>
    </header>

    <article class="letter">
      <div class="date">01 January 2050</div>
      <div class="recipient">
        <div class="recipient-name">Company (Pvt) Ltd.</div>
        <div>PO Box 3355 Birchfield St</div>
        <div>Sample City Country 3355</div>
      </div>
      <div class="salutation">Dear Martin Lowry,</div>
      <div class="letter-body">
        <p>Lorem ipsum dolor sit amet, consectetuer adipiscing elit, sed diam nonummy nibh euismod tincidunt ut laoreet dolore magna aliquam erat volutpat. Ut wisi enim ad minim veniam, quis nostrud exerci tation ullamcorper suscipit lobortis nisl ut aliquip ex ea commodo consequat. Duis dolore te feugait nulla facilisi. Nam liber tempor cum soluta nobis eleifend option congue nihil imperdiet doming id quod mazim placerat facer possim assum. Lorem ipsum dolor sit amet, consectetuer adipiscing elit, sed diam nonummy nibh euismod tincidunt ut laoreet dolore magna aliquam erat volutpat. Ut wisi enim ad minim veniam, quis nostrud exerci tation ullamcorper suscipit lobortis nisl ut aliquip ex ea commodo consequat.</p>
        <p>Consectetuer adipiscing elit, sed diam nonummy nibh euismod tincidunt ut laoreet dolore magna aliquam erat volutpat. Ut wisi enim ad minim veniam, quis nostrud exerci tation ullamcorper suscipit lobortis nisl ut aliquip ex ea commodo consequat. Consectetuer adipiscing elit, sed diam nonummy nibh euismod tincidunt ut laoreet dolore magna aliquam erat volutpat. Ut wisi enim ad minim veniam, quis nostrud exerci tation ullamcorper suscipit lobortis nisl ut aliquip ex ea commodo consequat.</p>
        <p>Consectetuer adipiscing elit, sed diam nonummy nibh euismod tincidunt ut laoreet dolore magna aliquam erat volutpat. Ut wisi enim ad minim veniam, quis nostrud exerci tation ullamcorper suscipit lobortis nisl ut aliquip ex ea commodo consequat. Consectetuer adipiscing elit, sed diam nonummy nibh euismod tincidunt ut laoreet dolore magna aliquam erat volutpat. Ut wisi enim ad minim veniam, quis nostrud exerci tation ullamcorper suscipit lobortis nisl ut aliquip ex ea commodo consequat.</p>
      </div>
      <div class="closing">Sincerely Yours</div>
      <div class="signature">Elliot James Harwell</div>
    </article>

    <svg class="footer-wedge" viewBox="0 1200 955 149" preserveAspectRatio="none" aria-hidden="true">
      <polygon fill="#9aab3f" points="0,1327 902,1235 300,1349 0,1349"/>
      <polygon fill="#1c1c1c" points="170,1349 955,1234 955,1349"/>
    </svg>
  </main>
</body>
</html>
```